Pomelo - Website for fruit & juice

- The location of the outlet is Fort Kochi in India.
- Fort Kochi is a tourist destination. And it attracts majorly French and Portuguese tourist due to the history of the place.
- The location had plenty of food joints & mostly provide local foods only without giving much options to tourist.
- Road side fruit shops don't look hygienic
- At Pomelo we are going to sell fresh fruits as well as fruit juices.
- Customers can pick their fruits and Pomelo staffs will squeeze/blend or slice it for them.
- There will be no e-commerce on the site (no buying of products through site)

Target Market(s)

Tourist & health conscious individuals who want to have fresh fruit or juice.

Coding

Coded - Design and coding required

Number of Pages Required

4 page

Font styles to use
Script

Colors

Designer to choose colors to be used in the design.

Requirements
Must have
• Back End. Editable website.
• Since it for fruits & juices, we will be selling fruits as per season or availability.
• Editable or back end will allow us to add or delete menus as per availability.
• The project much have 4 pages. Namely:
• - Home
• - Concept
• - Menu
• - Location & Contact
Nice to have
• Fresh feel of the website
Should not have
• E-commerce

```html
<!DOCTYPE html>
<html lang="en">
<head>
<meta charset="utf-8">
<title>Pomelo – Fresh Fruit &amp; Juice</title>
<link rel="stylesheet" href="https://fonts.googleapis.com/css2?family=Poppins:wght@300;400;500;600;700;800&display=swap">
<style>
:root{
  --green:#7cbc1e;
  --green-dark:#5e9612;
  --ink:#1f1f1f;
  --text:#6b6b6b;
  --muted:#9a9a9a;
  --line:#e6e6e6;
  --footer:#f4f4f4;
  --white:#ffffff;
  --orange:#f39a1e;
}
*{box-sizing:border-box;margin:0;padding:0}
html,body{width:1200px;height:3028px;overflow:hidden;background:var(--white)}
body{font-family:'Poppins',sans-serif;color:var(--text);position:relative}
.canvas{position:relative;width:1200px;height:3028px;overflow:hidden}

/* nav */
.site-nav{position:absolute;top:0;left:0;width:1200px;height:88px;background:var(--white);z-index:3}
.nav-links{position:absolute;top:34px;display:flex;gap:36px;font-size:15px;color:var(--ink)}
.nav-links.left{left:350px}
.nav-links.right{left:716px}
.nav-links .active{color:var(--green);border-bottom:2px solid var(--green);padding-bottom:4px}
.brand{position:absolute;left:540px;top:6px;width:120px;height:120px;border-radius:50%;background:var(--white);display:flex;align-items:center;justify-content:center;box-shadow:0 4px 12px rgba(0,0,0,.12)}
.brand span{font-weight:700;font-size:26px;color:var(--green)}

/* hero */
.hero{position:absolute;top:88px;left:0;width:1200px;height:580px;background:linear-gradient(180deg,#4a5a3c 0%,#2f4a2a 40%,#6d6a4e 70%,#8a8770 100%)}
.hero-scene{position:absolute;inset:0}
.hero-copy{position:absolute;top:170px;left:0;width:1200px;text-align:center;color:var(--white);font-size:44px;font-weight:500;line-height:54px}
.hero-copy .accent{color:#b8e04a}
.btn{display:inline-block;background:var(--green);color:var(--white);font-size:13px;font-weight:600;letter-spacing:.5px;padding:0 30px;height:46px;line-height:46px;border-radius:23px;text-transform:uppercase}
.hero .btn{position:absolute;left:524px;top:368px}

/* section headings */
.fruit-icon{display:block;width:34px;height:36px}
.section-title{color:var(--ink);font-weight:700;font-size:50px;line-height:58px}
.body-copy{font-size:12.5px;line-height:22px;color:var(--text)}
.body-copy .highlight{color:var(--green)}

/* origin */
.origin-photo{position:absolute;left:140px;top:860px;width:340px;height:230px;border-radius:50%/40%;background:radial-gradient(circle at 50% 40%,#f6a93a 0%,#e8891c 45%,#b58a4e 75%,#fff 76%)}
.origin-text{position:absolute;left:600px;top:770px;width:440px}
.origin-text .section-title{margin-top:8px}
.origin-text .body-copy{margin-top:22px}
.origin-text .body-copy+.body-copy{margin-top:12px}
.origin-text .btn{margin-top:38px}

.deco-fruit{position:absolute;border-radius:50%;border:2px solid #efefef}

/* menu */
.menu-head{position:absolute;top:1212px;left:0;width:1200px;text-align:center}
.menu-head .fruit-icon{margin:0 auto}
.menu-head h2{font-size:34px;font-weight:700;color:var(--ink);margin-top:4px}
.menu-head p{font-size:12.5px;line-height:20px;width:520px;margin:12px auto 0}
.menu-grid{position:absolute;top:1408px;left:152px;width:896px;height:640px;display:grid;grid-template-columns:296px 296px 296px;grid-template-rows:316px 316px;gap:8px}
.tile{position:relative}
.tile-split{display:grid;grid-template-columns:1fr 1fr;gap:8px}
.story-box{position:absolute;left:38px;top:44px;width:220px;height:196px;background:var(--green);color:var(--white);text-align:center;padding-top:52px}
.story-box small{display:block;font-size:12px}
.story-box strong{display:block;font-size:15px;font-weight:700;margin-top:4px;letter-spacing:.5px}
.story-box em{display:block;font-style:normal;font-size:11px;font-weight:600;margin-top:16px}

/* about */
.about-text{position:absolute;left:210px;top:2150px;width:420px;text-align:center}
.about-text .title-block{display:inline-block;text-align:left}
.about-text .fruit-icon{margin-left:190px}
.about-text .body-copy{margin-top:22px}
.about-text .body-copy+.body-copy{margin-top:12px}
.about-text .btn{margin-top:36px}
.about-ring{position:absolute;left:690px;top:2172px;width:400px;height:400px;border-radius:50%;border:2px solid #d8eac0;display:flex;align-items:center;justify-content:center}
.about-photo{width:360px;height:360px;border-radius:50%;background:radial-gradient(circle at 45% 50%,#f7c23a 0%,#f09a2a 35%,#d9473a 60%,#f7f2e8 80%)}
.pineapple{position:absolute;left:-30px;top:2060px;width:170px;height:400px;border-radius:50% 50% 45% 45%;background:linear-gradient(180deg,rgba(0,0,0,0) 0%,rgba(0,0,0,.04) 30%,rgba(0,0,0,.07) 100%)}

/* footer */
.site-footer{position:absolute;top:2710px;left:0;width:1200px;height:318px;background:var(--footer)}
.footer-cols{position:absolute;top:42px;left:150px;display:grid;grid-template-columns:232px 232px 232px 232px}
.footer-cols h4{font-size:13px;font-weight:600;color:var(--ink);margin-bottom:14px}
.footer-cols li{list-style:none;font-size:11px;line-height:19px;color:var(--muted)}
.contact-line{display:flex;gap:8px;align-items:flex-start;font-size:11px;line-height:17px;color:var(--muted);margin-bottom:10px}
.contact-line svg{flex:none;margin-top:2px}
.socials{display:flex;gap:18px;margin-top:12px;padding-left:2px}
.socials span{width:14px;height:14px;border-radius:50%;background:#555}
.newsletter p{font-size:11px;line-height:17px;color:var(--muted)}
.news-input{margin-top:14px;width:196px;height:34px;border:1px solid var(--line);border-radius:17px;background:var(--white);font-size:11px;color:var(--muted);padding:0 16px;line-height:32px}
.newsletter .btn{margin-top:14px;height:34px;line-height:34px;font-size:11px;padding:0 26px}
.copyright{position:absolute;bottom:18px;left:0;width:1200px;text-align:center;font-size:11px;color:var(--muted);border-top:1px solid var(--line);padding-top:14px}
</style>
</head>
<body>
<div class="canvas">

  <header class="site-nav">
    <nav class="nav-links left"><span class="active">Home</span><span>Concept</span></nav>
    <div class="brand"><span>Pomelo</span></div>
    <nav class="nav-links right"><span>Menu</span><span>Contact</span></nav>
  </header>

  <section class="hero">
    <div class="hero-scene" role="img" aria-label="Houseboat on a backwater lake lined with palm trees, a glass of juice in the corner"></div>
    <h1 class="hero-copy">We make juice from the fresh fruits<br><span class="accent">that you pick up yourself</span><br>from the fruit basket</h1>
    <span class="btn">Contact us</span>
  </section>

  <div class="deco-fruit" style="left:40px;top:800px;width:110px;height:110px"></div>
  <div class="deco-fruit" style="left:1000px;top:760px;width:90px;height:90px"></div>

  <section class="origin">
    <div class="origin-photo" role="img" aria-label="Wooden bowl of fresh oranges beside a red apple"></div>
    <div class="origin-text">
      <svg class="fruit-icon" viewBox="0 0 34 36"><circle cx="17" cy="21" r="13" fill="var(--orange)"/><path d="M17 8 C15 4 18 2 20 2" stroke="#6a8f1e" stroke-width="2" fill="none"/><ellipse cx="22" cy="6" rx="5" ry="2.5" fill="var(--green)"/></svg>
      <h2 class="section-title">Origin of the<br>Concept</h2>
      <p class="body-copy">Fort Kochi draws visitors from across the world, yet few places offer fresh fruit they can trust. <span class="highlight">Pick your fruit, we squeeze it for you.</span></p>
      <p class="body-copy">Our idea began with a clean fruit counter where guests choose their own fruit and our staff blend, press or slice it on the spot while they watch.</p>
      <span class="btn">Read more</span>
    </div>
  </section>

  <section>
    <div class="menu-head">
      <svg class="fruit-icon" viewBox="0 0 34 36"><circle cx="17" cy="21" r="13" fill="var(--orange)"/><path d="M17 8 C15 4 18 2 20 2" stroke="#6a8f1e" stroke-width="2" fill="none"/><ellipse cx="22" cy="6" rx="5" ry="2.5" fill="var(--green)"/></svg>
      <h2>Manu</h2>
      <p>Our menu changes with the seasons, so every glass and plate is made from the ripest fruit of the day.</p>
    </div>
    <div class="menu-grid">
      <div class="tile" role="img" aria-label="Orange juice with sliced oranges" style="background:linear-gradient(135deg,#f7b640,#e5731c)"></div>
      <div class="tile" role="img" aria-label="Mixed fresh fruit" style="background:linear-gradient(135deg,#e9c46a,#c9543a)">
        <div class="story-box"><small>Visit our</small><strong>STORY OF JUICE</strong><em>READ MORE</em></div>
      </div>
      <div class="tile tile-split">
        <div role="img" aria-label="Red and green apples" style="background:linear-gradient(135deg,#d94b3a,#9cc13a)"></div>
        <div role="img" aria-label="Green smoothie in a glass" style="background:linear-gradient(180deg,#8cc64a,#4e8e2a)"></div>
      </div>
      <div class="tile" role="img" aria-label="Hands holding fresh strawberries" style="background:linear-gradient(135deg,#e8433e,#b0202a)"></div>
      <div class="tile" role="img" aria-label="Blueberry smoothie with blueberries" style="background:linear-gradient(135deg,#7a6a8e,#2f2a48)"></div>
      <div class="tile" role="img" aria-label="Ripe fruit hanging on a tree" style="background:linear-gradient(135deg,#a8c848,#4d7a2a)"></div>
    </div>
  </section>

  <section>
    <div class="pineapple" role="img" aria-label="Faint pineapple decoration"></div>
    <div class="about-text">
      <div class="title-block">
        <svg class="fruit-icon" viewBox="0 0 34 36"><circle cx="17" cy="21" r="13" fill="var(--orange)"/><path d="M17 8 C15 4 18 2 20 2" stroke="#6a8f1e" stroke-width="2" fill="none"/><ellipse cx="22" cy="6" rx="5" ry="2.5" fill="var(--green)"/></svg>
        <h2 class="section-title">About the<br>Pomelo</h2>
      </div>
      <p class="body-copy">Pomelo is a small fruit bar in the heart of Fort Kochi, serving fresh fruit and juice to travellers and locals who care about what they eat and drink each day.</p>
      <p class="body-copy">We work with nearby farms, keep our counter spotless and make each order by hand, so every visit tastes as fresh as the fruit you picked.</p>
      <span class="btn">Read more</span>
    </div>
    <div class="about-ring"><div class="about-photo" role="img" aria-label="Glass of orange juice surrounded by oranges, strawberries and kiwi"></div></div>
  </section>

  <footer class="site-footer">
    <div class="footer-cols">
      <div>
        <h4>Quick Links</h4>
        <ul><li>Home</li><li>Concept</li><li>Menu</li><li>Location</li><li>Contact</li></ul>
      </div>
      <div>
        <h4>Customer Support</h4>
        <ul><li>Help and Ordering</li><li>Privacy Policy</li><li>Return &amp; Cancellation</li><li>Delivery Schedule</li><li>Get a Call</li><li>Online Enquiry</li><li>My Account</li></ul>
      </div>
      <div>
        <h4>Contact Info</h4>
        <div class="contact-line"><svg width="12" height="14" viewBox="0 0 12 14"><path d="M6 0a5 5 0 0 0-5 5c0 4 5 9 5 9s5-5 5-9a5 5 0 0 0-5-5zm0 7a2 2 0 1 1 0-4 2 2 0 0 1 0 4z" fill="var(--green)"/></svg><span>12 Rose Street, Fort Kochi,<br>Kerala 682001, India</span></div>
        <div class="contact-line"><svg width="12" height="12" viewBox="0 0 12 12"><path d="M2.5 0 4.5 3 3 4.5a7 7 0 0 0 4.5 4.5L9 7.5l3 2-1 2.5C5 12 0 7 0 1z" fill="var(--green)"/></svg><span>+91 484 555 0192</span></div>
        <div class="contact-line"><svg width="13" height="10" viewBox="0 0 13 10"><rect x=".5" y=".5" width="12" height="9" fill="none" stroke="var(--green)"/><path d="M.5.5l6 5 6-5" fill="none" stroke="var(--green)"/></svg><span>hello@pomelo.in</span></div>
        <div class="socials"><span></span><span></span><span></span><span></span></div>
      </div>
      <div class="newsletter">
        <h4>Newsletter</h4>
        <p>Enter your email to hear about our seasonal fruit and menu news.</p>
        <div class="news-input">Enter your email</div>
        <span class="btn">Subscribe</span>
      </div>
    </div>
    <div class="copyright">© Copyright 2024</div>
  </footer>

</div>
</body>
</html>
```